Cosmetic injections clinic needs a fresh looking business card

We need a business card using the supplied logo and color scheme to attract future clients to our clinic. It should be modern and fresh, eye catching and not too busy. Simple and to the point is best. I would like two sided designs with the front indicating address and contact information, and the back in full color with white logo and descriptive information also provided.
Target Market(s)
Clients looking for non surgical beauty enhancements.
Contact Information for Business Card
MeloraSkin
14, 618 Birchmont Way
St. Albert, Alberta
K2P 7W3
Phone: 587-412-6630
Email: info@meloraskin.com
Requirements
Must have
- -Logo supplied with the name and address of the clinic
- -Back of card in full color with white logo with A small line of text indicating both of the following: Anti aging consultants and cosmetic injectables
- Located inside the Voyager Wellness Group

```html
<!DOCTYPE html>
<html lang="en">
<head>
<meta charset="utf-8">
<title>MeloraSkin Business Card</title>
<link href="https://fonts.googleapis.com/css2?family=Poppins:wght@400;500;600&display=swap" rel="stylesheet">
<style>
  :root {
    --backdrop: #2a2b2e;
    --purple: #7058a4;
    --purple-light: #7d66b0;
    --pink: #e062a0;
    --teal: #25b4bc;
    --paper: #ffffff;
    --ink-grey: #8d8a7f;
    --white: #ffffff;
  }
  * { box-sizing: border-box; margin: 0; padding: 0; }
  html, body {
    width: 1200px; height: 1000px; overflow: hidden;
    background: var(--backdrop);
    font-family: "Poppins", sans-serif;
  }
  .sheet {
    position: relative; width: 1200px; height: 1000px;
  }
  .card {
    position: absolute; left: 250px; width: 700px; height: 400px;
    border-radius: 4px; overflow: hidden;
    box-shadow: 0 14px 30px rgba(0,0,0,.35);
  }
  /* Front */
  .card--front { top: 60px; background: var(--paper); }
  .brand-mark {
    position: absolute; left: 60px; top: 50px;
    width: 200px; height: 200px;
    display: flex; align-items: center; justify-content: center;
  }
  .brand-mark__circle {
    width: 170px; height: 170px; border-radius: 50%;
    background: var(--purple);
  }
  .contact {
    position: absolute; left: 330px; top: 42px; right: 40px;
  }
  .contact__name {
    font-size: 44px; font-weight: 600; color: var(--purple);
    line-height: 1; margin-bottom: 20px; letter-spacing: -0.5px;
  }
  .contact__row {
    display: flex; align-items: flex-start; gap: 12px;
    font-size: 18px; color: var(--ink-grey); line-height: 1.35;
    margin-bottom: 6px;
  }
  .contact__icon { width: 20px; height: 20px; flex: none; margin-top: 2px; }
  .contact__clinic { color: var(--purple); font-weight: 500; }
  .band {
    position: absolute; left: 0; right: 0; bottom: 0; height: 66px;
    background: var(--purple);
    display: flex; align-items: center; padding-left: 40px;
    color: var(--white); font-size: 18px; letter-spacing: .2px;
  }
  /* Back */
  .card--back {
    top: 540px;
    background: linear-gradient(135deg, var(--purple-light), var(--purple));
  }
  .back-brand {
    position: absolute; left: 0; right: 0; top: 120px;
    display: flex; align-items: center; justify-content: center; gap: 18px;
  }
  .back-brand__circle {
    width: 64px; height: 64px; border-radius: 50%; background: var(--white);
  }
  .back-brand__name {
    font-size: 48px; font-weight: 600; color: var(--white); letter-spacing: -0.5px;
  }
  .tagline {
    position: absolute; left: 0; right: 0; top: 250px; text-align: center;
    color: var(--white); font-size: 19px; letter-spacing: .3px;
  }
</style>
</head>
<body>
<main class="sheet">

  <section class="card card--front" aria-label="Card front">
    <div class="brand-mark"><div class="brand-mark__circle"></div></div>

    <div class="contact">
      <div class="contact__name">MeloraSkin</div>

      <div class="contact__row">
        <svg class="contact__icon" viewBox="0 0 24 24" aria-hidden="true">
          <circle cx="12" cy="12" r="11" fill="var(--purple)"/>
          <path d="M8.5 6.5l2 2-1.2 1.6c.8 1.7 2 2.9 3.6 3.6l1.6-1.2 2 2-1.3 1.8c-4.2-.4-8-4.2-8.4-8.4z" fill="#fff"/>
        </svg>
        <span>587-412-6630</span>
      </div>

      <div class="contact__row">
        <svg class="contact__icon" viewBox="0 0 24 24" aria-hidden="true">
          <circle cx="12" cy="12" r="11" fill="var(--purple)"/>
          <g fill="none" stroke="#fff" stroke-width="1.4">
            <circle cx="12" cy="12" r="6.5"/>
            <ellipse cx="12" cy="12" rx="2.8" ry="6.5"/>
            <line x1="5.5" y1="12" x2="18.5" y2="12"/>
          </g>
        </svg>
        <span>info@meloraskin.com</span>
      </div>

      <div class="contact__row">
        <svg class="contact__icon" viewBox="0 0 24 24" aria-hidden="true">
          <path d="M12 2a7 7 0 0 0-7 7c0 5 7 13 7 13s7-8 7-13a7 7 0 0 0-7-7z" fill="var(--purple)"/>
          <circle cx="12" cy="9" r="2.6" fill="#fff"/>
        </svg>
        <span>
          <span class="contact__clinic">MeloraSkin</span><br>
          14, 618 Birchmont Way<br>
          St. Albert, Alberta<br>
          K2P 7W3
        </span>
      </div>
    </div>

    <div class="band">Located inside the Voyager Wellness Group</div>
  </section>

  <section class="card card--back" aria-label="Card back">
    <div class="back-brand">
      <div class="back-brand__circle"></div>
      <div class="back-brand__name">MeloraSkin</div>
    </div>
    <p class="tagline">Anti Aging Consultants &amp; Cosmetic Injectables</p>
  </section>

</main>
</body>
</html>
```